New Snazzy yet professinoal business card updated for todays consumer for a Real Estate Professional

I work in a family owned real estate business where we specialize in sales (buyer/seller) and property management. I would like a snazzy business card that will set me apart from other agents while maintaining its professional appearance. I would like to use the front and back of the card incorporating the business logo on the front with pictures and my personal logo on the back side. I have to have the TPXN symbol which I have attached. Card must be easy to read, distinguishable, and professional. Old card with contact information attached. My email has changed to Milo@MiloBrentwickHomes.com

Target Market(s)

Home Sellers, Home Buyers, Business Professionals, Marketing Services,

Industry/Entity Type

Real Estate Agent

Contact Information for Business Card

Professional business card to stand apart from other agents while maintaining a professional appeal.

Font styles to use
Serif

Colors
ec1f27
fbee3e
0455a3

Requirements
Must have
• Must have contact information clear, easy to read. legible
Nice to have
• My picture.

```html
<!DOCTYPE html>
<html lang="en">
<head>
<meta charset="utf-8">
<title>Milo Brentwick Homes – Business Card</title>
<link rel="stylesheet" href="https://fonts.googleapis.com/css2?family=Open+Sans:ital,wght@0,400;0,600;0,700;1,400&display=swap">
<style>
  :root {
    --navy: #233a7e;
    --red: #c8202f;
    --ink: #3d3d3d;
    --paper: #ffffff;
    --backdrop: #e9e7e4;
    --photo-top: #e4e1de;
    --photo-mid: #c99c86;
    --photo-bottom: #2b2d33;
    --badge-fill: #cfdcee;
    --badge-line: #7f9cc8;
  }
  * { box-sizing: border-box; margin: 0; padding: 0; }
  html, body {
    width: 1200px; height: 633px; overflow: hidden;
    background: var(--backdrop);
    font-family: "Open Sans", sans-serif;
  }
  .stage { position: relative; width: 1200px; height: 633px; }

  .card {
    position: absolute; top: 163px; width: 540px; height: 306px;
    overflow: hidden; box-shadow: 0 4px 10px rgba(0,0,0,.22);
  }

  /* Front */
  .card-front { left: 45px; background: var(--paper); }
  .brand-band { position: absolute; left: 0; top: 24px; width: 30px; height: 68px; background: var(--navy); }
  .brand {
    position: absolute; left: 40px; top: 34px;
    display: flex; align-items: center; gap: 10px;
    color: var(--navy); font-size: 19px; font-weight: 600; line-height: 23px;
  }
  .brand .dot { flex: none; width: 14px; height: 14px; border-radius: 50%; background: var(--red); }
  .brand .homes { display: block; letter-spacing: 6.4px; }

  .agent { position: absolute; left: 35px; top: 108px; }
  .agent-name { color: var(--navy); font-size: 19px; font-weight: 700; line-height: 24px; letter-spacing: .2px; }
  .agent-title { color: var(--red); font-size: 14px; line-height: 18px; }
  .agent-email { color: var(--ink); font-size: 14px; font-style: italic; line-height: 26px; }

  .phones { position: absolute; left: 35px; top: 180px; list-style: none; }
  .phones li { display: flex; align-items: center; gap: 8px; height: 20px; font-size: 14.5px; color: var(--ink); }
  .phones svg { width: 14px; height: 14px; fill: var(--navy); }

  .address { position: absolute; left: 33px; top: 250px; font-size: 14.5px; line-height: 20px; color: var(--ink); font-style: normal; }
  .listing-badge {
    display: inline-block; width: 38px; height: 14px; margin-left: 6px; vertical-align: -2px;
    background: var(--badge-fill); border: 1px solid var(--badge-line);
  }

  .portrait {
    position: absolute; right: 0; top: 0; width: 258px; height: 306px;
    background: linear-gradient(180deg, var(--photo-top) 0%, var(--photo-mid) 45%, var(--photo-bottom) 80%);
  }

  /* Back */
  .card-back { left: 615px; background: var(--navy); color: var(--paper); }
  .back-brand {
    position: absolute; left: 0; right: 0; top: 118px;
    display: flex; align-items: center; justify-content: center; gap: 12px;
    font-size: 24px; font-weight: 600; letter-spacing: .5px;
  }
  .back-brand .dot { width: 16px; height: 16px; border-radius: 50%; background: var(--paper); }
  .web {
    position: absolute; left: 0; right: 0; top: 256px;
    text-align: center; font-size: 14.5px; letter-spacing: 3px;
  }
</style>
</head>
<body>
<main class="stage">
  <section class="card card-front" aria-label="Card front">
    <div class="brand-band"></div>
    <div class="brand"><span class="dot"></span><span>MILO BRENTWICK<span class="homes">HOMES</span></span></div>

    <div class="agent">
      <h1 class="agent-name">MILO BRENTWICK</h1>
      <p class="agent-title">REALTOR, MBA, MPH</p>
      <p class="agent-email">Milo@MiloBrentwickHomes.com</p>
    </div>

    <ul class="phones">
      <li><svg viewBox="0 0 24 24"><path d="M6.6 10.8a15 15 0 0 0 6.6 6.6l2.2-2.2a1 1 0 0 1 1-.25 11.4 11.4 0 0 0 3.6.57 1 1 0 0 1 1 1V20a1 1 0 0 1-1 1A17 17 0 0 1 3 4a1 1 0 0 1 1-1h3.5a1 1 0 0 1 1 1c0 1.25.2 2.45.57 3.6a1 1 0 0 1-.25 1z"/></svg>555.210.1020</li>
      <li><svg viewBox="0 0 24 24"><path d="M7 1h10a2 2 0 0 1 2 2v18a2 2 0 0 1-2 2H7a2 2 0 0 1-2-2V3a2 2 0 0 1 2-2zm0 3v14h10V4z"/></svg>555.208.5893</li>
      <li><svg viewBox="0 0 24 24"><path d="M6 2h12v6H6zM3 9h18a1 1 0 0 1 1 1v7h-4v5H6v-5H2v-7a1 1 0 0 1 1-1zm5 7v4h8v-4z"/></svg>555.210.1027</li>
    </ul>

    <address class="address">48 Larkmoor plaza fenwick<br>Mississippi 39000<span class="listing-badge" aria-label="TPXN listing badge"></span></address>

    <div class="portrait" role="img" aria-label="Portrait photo of the agent in a dark suit and pink tie"></div>
  </section>

  <section class="card card-back" aria-label="Card back">
    <div class="back-brand"><span class="dot"></span>Milo Brentwick Homes</div>
    <p class="web">www.webname.com</p>
  </section>
</main>
</body>
</html>
```